Business Performance Improvement Book Cover Design Project

We need a book cover design for a new company, based in Eastern Australia, called Varrow Global. We advise clients on process improvement, continuous improvement and business performance improvement, especially in the manufacturing areas and Fast Moving Consumer Goods industries.
We have a written a book designed to demonstrate our very high calibre of knowledge and to use as a marketing tool for prospective clients. We hope to give it out at training seminars and as a comprehensive business card.

Title of the book is: An integrated path to Operational Results Growth.
Subtitle: Shape a Steady Progress method to match your workplace values.
Author: by Martin Varrow
Back Cover: No need for a bar code in this edition. An important aspect is that we will distribute by hand. Text below for back page.

'For the experienced Business Performers, this book is designed to offer an insight into the advantages and an example of an approach to Business Improvement. It is not the only way but it is tried and tested in world class companies and it works. For those new to Continuous Improvement, it offers a helpful introduction to a holistic business improvement system, an overview of important success factors and pitfalls, recommendations on how to implement tools and methods and a quick guide to see when to use which tools. '

'Consultancies are one of many tools management teams can engage and management must make sure the consultants tailor their approach to suit its business needs and culture and not vice versa.'

End of text for back cover.

Business Performance Improvement is also known as or can include:
Continuous Improvement
Process Improvement
Lean Six Sigma
Operational Excellence
Total Productive Maintenance
Harlow Assembly Method
Total Quality Management
Business Process Re engineering
Output Levers
=
Varrow Global

The book size is 175 x 240 mm and will need a 10-15mm bleed. The spine is not known at this stage exactly and will need to be updated once the printing is finished but I suggest a 10mm until I have the exact size.

Our company colours are Pantone 288, R0,G75,B141, C100,M79,Y17,K3. Attached are some other publications that give a sense of what we like to portray, Some words which might add to this are: professional, elegance, quality, sleek.

Reason: After receiving the designs, I realised that I needed to update the brief with more and better quality information for designers to work with.

Target Market(s)

people in the accounting and insolvency industries, production managers and CEOs, Chief Operating Officers, members of the executive team of large companies and GMs of small companies.

Industry/Entity Type

Marketing

Requirements
Must have
• Communicate an image that shows an improvement or increase of something.
Very professional and elegant
Emphasis on the words 'Business Performance Improvement' in the title, subtitle also important
Must appeal to a high-end of the market audience
Nice to have
• Recommendation for your cover to be gloss or matt in print
Image can be indirectly related to money but not specifically
Somehow that it matches or is not so different to the attached brochure
Should not have
• Not be too loud or commercial
Book jacket. WIll be printed as soft cover first run and hard cover 2nd run

```html
<!DOCTYPE html>
<html lang="en">
<head>
<meta charset="utf-8">
<title>An integrated path to Operational Results Growth – Book Jacket</title>
<link rel="stylesheet" href="https://fonts.googleapis.com/css2?family=Alegreya:ital,wght@0,400;0,700;0,800;1,400&display=swap">
<style>
  :root {
    --back-navy: #0c3868;
    --front-sky: #1b4d8b;
    --base-navy: #0a3566;
    --ink-white: #ffffff;
    --ink-soft: #dbe5f1;
    --spine-edge: #ffffff;
  }
  html, body {
    margin: 0;
    padding: 0;
    width: 1200px;
    height: 832px;
    overflow: hidden;
    background: var(--back-navy);
  }
  .jacket {
    position: relative;
    width: 1200px;
    height: 832px;
    overflow: hidden;
    font-family: "Alegreya", Georgia, serif;
    color: var(--ink-white);
  }
  .back-cover {
    position: absolute;
    left: 0; top: 0;
    width: 586px; height: 832px;
    background: var(--back-navy);
  }
  .back-blurb {
    position: absolute;
    left: 78px; top: 96px;
    width: 430px;
    font-size: 14.5px;
    line-height: 22px;
    color: var(--ink-soft);
    text-align: left;
  }
  .back-blurb p { margin: 0 0 18px; }
  .back-blurb .pull {
    font-style: italic;
    color: var(--ink-white);
  }
  .publisher {
    position: absolute;
    left: 0; width: 586px;
    top: 683px;
    text-align: center;
    font-style: italic;
    font-size: 12.5px;
    line-height: 14.5px;
  }
  .publisher-mark {
    display: inline-flex;
    align-items: center;
    gap: 6px;
    font-style: normal;
    font-weight: 700;
    font-size: 17px;
    line-height: 20px;
    margin-bottom: 8px;
  }
  .publisher-mark .dot {
    width: 10px; height: 10px;
    border-radius: 50%;
    background: var(--ink-white);
  }
  .publisher p { margin: 0; }

  .front-art {
    position: absolute;
    left: 586px; top: 0;
    width: 614px; height: 832px;
  }
  .spine {
    position: absolute;
    left: 586px; top: 0;
    width: 29px; height: 832px;
  }
  .spine-mark {
    position: absolute;
    left: 0; top: 0;
    width: 29px; height: 94px;
    background: var(--spine-edge);
    display: flex;
    align-items: center;
    justify-content: center;
  }
  .spine-mark span {
    writing-mode: vertical-rl;
    color: var(--base-navy);
    font-weight: 700;
    font-size: 10px;
    letter-spacing: 0.3px;
  }
  .spine-title {
    position: absolute;
    left: 3px; top: 110px;
    writing-mode: vertical-rl;
    font-size: 17px;
    letter-spacing: 0.6px;
    white-space: nowrap;
  }
  .spine-author {
    position: absolute;
    left: 8px; top: 654px;
    writing-mode: vertical-rl;
    font-style: italic;
    font-size: 9px;
    white-space: nowrap;
  }
  .front-title {
    position: absolute;
    right: 28px; top: 588px;
    margin: 0;
    text-align: right;
    font-weight: 800;
    font-size: 38px;
    line-height: 46px;
    letter-spacing: 0.2px;
  }
  .front-subtitle {
    position: absolute;
    right: 28px; top: 738px;
    margin: 0;
    text-align: right;
    font-style: italic;
    font-size: 16px;
    line-height: 20px;
    color: var(--ink-soft);
  }
  .front-author {
    position: absolute;
    left: 615px; width: 585px;
    top: 799px;
    margin: 0;
    text-align: center;
    font-style: italic;
    font-size: 12.5px;
  }
</style>
</head>
<body>
<main class="jacket">
  <section class="back-cover">
    <div class="back-blurb">
      <p>For the experienced Business Performers, this book is designed to offer an insight into the advantages and an example of an approach to Business Improvement. It is not the only way but it is tried and tested in world class companies and it works. For those new to Continuous Improvement, it offers a helpful introduction to a holistic business improvement system, an overview of important success factors and pitfalls, recommendations on how to implement tools and methods and a quick guide to see when to use which tools.</p>
      <p class="pull">Consultancies are one of many tools management teams can engage and management must make sure the consultants tailor their approach to suit its business needs and culture and not vice versa.</p>
    </div>
    <div class="publisher">
      <div class="publisher-mark"><span class="dot"></span>Varrow Global</div>
      <p>Varrow Global Pty Limited</p>
      <p>118 Kestrel Rd</p>
      <p>Alderby NSW 2290</p>
      <p>Australia</p>
      <p>+61 2 5550 0172</p>
      <p>ABN No. 00123456789 &nbsp;|&nbsp; ACN No. 123456789</p>
    </div>
  </section>

  <svg class="front-art" viewBox="0 0 614 832" xmlns="http://www.w3.org/2000/svg">
    <defs>
      <linearGradient id="rise-tone" x1="0" y1="0" x2="1" y2="0">
        <stop offset="0" stop-color="#f0a24a"/>
        <stop offset="0.15" stop-color="#e0553a"/>
        <stop offset="0.45" stop-color="#c42a3a"/>
        <stop offset="0.8" stop-color="#8c1435"/>
        <stop offset="1" stop-color="#4a0a26"/>
      </linearGradient>
      <linearGradient id="rise-fade" x1="0" y1="0" x2="0" y2="1">
        <stop offset="0" stop-color="#000" stop-opacity="0.25"/>
        <stop offset="1" stop-color="#000" stop-opacity="0"/>
      </linearGradient>
      <radialGradient id="horizon-glow" cx="0.5" cy="0.5" r="0.5">
        <stop offset="0" stop-color="#dfeaf6" stop-opacity="0.6"/>
        <stop offset="1" stop-color="#dfeaf6" stop-opacity="0"/>
      </radialGradient>
    </defs>
    <rect class="sky" x="0" y="0" width="614" height="832" fill="var(--front-sky)"/>
    <ellipse cx="340" cy="260" rx="380" ry="110" fill="url(#horizon-glow)"/>
    <g class="growth-steps" role="img" aria-label="Rising columns in warm orange to deep red tones showing steady growth">
      <polygon points="0,330 80,330 80,305 160,305 160,284 240,284 240,262 320,262 320,240 400,240 400,219 480,219 480,198 560,198 560,176 614,176 614,510 0,648" fill="url(#rise-tone)"/>
      <polygon points="0,330 80,330 80,305 160,305 160,284 240,284 240,262 320,262 320,240 400,240 400,219 480,219 480,198 560,198 560,176 614,176 614,510 0,648" fill="url(#rise-fade)"/>
      <g stroke="#0a3566" stroke-opacity="0.35" stroke-width="2">
        <line x1="80" y1="305" x2="80" y2="630"/>
        <line x1="160" y1="284" x2="160" y2="611"/>
        <line x1="240" y1="262" x2="240" y2="592"/>
        <line x1="320" y1="240" x2="320" y2="574"/>
        <line x1="400" y1="219" x2="400" y2="555"/>
        <line x1="480" y1="198" x2="480" y2="537"/>
        <line x1="560" y1="176" x2="560" y2="518"/>
      </g>
    </g>
    <polygon class="base-band" points="0,648 614,510 614,832 0,832" fill="var(--base-navy)"/>
  </svg>

  <aside class="spine">
    <div class="spine-mark"><span>Varrow Global</span></div>
    <div class="spine-title">An integrated path to Operational Results Growth</div>
    <div class="spine-author">Martin Varrow B. Mech Eng., M. Sc (Eng)</div>
  </aside>

  <h1 class="front-title">An integrated path<br>to Operational Results<br>Growth</h1>
  <p class="front-subtitle">Shape a Steady Progress method<br>to match your workplace values</p>
  <p class="front-author">Martin Varrow B. Mech Eng., M. Sc (Eng)</p>
</main>
</body>
</html>
```